Quorvex clinic business card - double sided for young clinic

I require business cards for my aesthetic clinic specialising in the below treatments. I would like the cards to be modern as my clinic base are young 22-35 years old. I require my logo on it and would like the edges to be rounded.

I have an aesthetic clinic specialising in :
Quorvex
Lip Enhancement
Chemical Peels
Facial Fillers
Non Surgical Face Lift

I would the cards to have the following information on them:
My logo - (in grey/silver)
address
Phone number
services

Colours :
White/grey/silver and red

a nice image on there, perhaps a set of lips as this is a main service i deliver

Company Name: PDA Address: 52 Farrowmere Road, 4 Brackwell High Street, KT9 4WQ Phone: 0208 794 2160 Website: www.penningtondoweaesthetics.co.uk

Target Market(s)

clinics 22-45 years old mainly female

Industry/Entity Type

Business

Contact Information for Business Card

as above

Requirements
Must have
• logo
• Address
• Email
• Phone number
• Services i offer
Nice to have
• images

```html
<!DOCTYPE html>
<html lang="en">
<head>
<meta charset="utf-8">
<title>PDA Business Card</title>
<link href="https://fonts.googleapis.com/css2?family=Great+Vibes&family=Libre+Baskerville:ital,wght@0,400;0,700;1,400&display=swap" rel="stylesheet">
<style>
  :root {
    --red: #d11414;
    --red-deep: #b80e0e;
    --grey: #e6e6e6;
    --grey-dark: #d4d4d4;
    --white: #ffffff;
    --page: #ffffff;
  }
  * { margin: 0; padding: 0; box-sizing: border-box; }
  html, body { width: 960px; height: 1200px; overflow: hidden; background: var(--page); }
  .sheet { position: relative; width: 960px; height: 1200px; }
  .card {
    position: absolute; left: 100px; width: 760px; height: 433px; overflow: hidden;
    box-shadow: 0 4px 10px rgba(0,0,0,0.35);
    font-family: "Libre Baskerville", Georgia, serif;
  }
  .card--front { top: 150px; background: var(--red); }
  .card--back { top: 640px; background: var(--grey-dark); }
  .card__shapes { position: absolute; inset: 0; width: 760px; height: 433px; }

  .brand { position: absolute; text-align: center; color: var(--red); }
  .brand__mark { width: 150px; height: 150px; margin: 0 auto 12px; border-radius: 50%; background: var(--red); }
  .brand__name { font-weight: 400; text-transform: uppercase; line-height: 1.1; white-space: nowrap; }
  .brand__name--small { font-size: 21px; letter-spacing: 2px; }
  .brand__name--large { font-size: 34px; letter-spacing: 3px; }
  .card--front .brand { left: 10px; top: 150px; width: 350px; }
  .card--back .brand { left: 0; top: 180px; width: 330px; }
  .card--back .brand__mark { width: 130px; height: 130px; margin-bottom: 10px; }
  .card--back .brand__name--small { font-size: 19px; }
  .card--back .brand__name--large { font-size: 30px; }

  .site-link {
    position: absolute; left: 8px; top: 405px; color: var(--red);
    font-style: italic; font-weight: 700; font-size: 14px; white-space: nowrap;
  }

  .treatments { position: absolute; left: 455px; top: 70px; color: var(--white); }
  .treatments__title { display: flex; align-items: center; gap: 8px; font-size: 18px; font-weight: 700; margin-bottom: 26px; }
  .treatments__list { list-style: none; }
  .treatments__item {
    display: flex; align-items: center; gap: 14px; white-space: nowrap;
    font-style: italic; font-size: 18px; margin-bottom: 20px; padding-left: 10px;
  }
  .treatments__item svg { flex: none; }

  .owner-name {
    position: absolute; right: 30px; top: 25px; width: 260px; color: var(--red);
    font-family: "Great Vibes", cursive; font-size: 64px; line-height: 0.95;
  }
  .owner-name span { display: block; }
  .owner-name span + span { padding-left: 60px; }

  .contact { position: absolute; right: 10px; top: 278px; list-style: none; color: var(--white); }
  .contact__row {
    display: flex; justify-content: flex-end; align-items: center; gap: 10px;
    font-style: italic; font-size: 18px; height: 34px; white-space: nowrap;
  }
  .contact__row--small { font-size: 16px; }
  .contact__row svg { flex: none; }
</style>
</head>
<body>
<main class="sheet">

  <section class="card card--front" aria-label="Card front">
    <svg class="card__shapes" viewBox="0 0 760 433">
      <path role="img" aria-label="Light grey area with a fine geometric pattern" d="M0,58 C250,45 420,230 445,433 L0,433 Z" fill="var(--grey)"/>
    </svg>

    <div class="brand">
      <div class="brand__mark"></div>
      <p class="brand__name brand__name--small">Pennington Dowe</p>
      <p class="brand__name brand__name--large">Aesthetics</p>
    </div>

    <p class="site-link">http://www.penningtondoweaesthetics.co.uk/</p>

    <div class="treatments">
      <h2 class="treatments__title">
        <svg width="34" height="38" viewBox="0 0 34 38" aria-hidden="true">
          <rect x="3" y="5" width="28" height="31" rx="3" fill="none" stroke="#fff" stroke-width="2"/>
          <rect x="11" y="1" width="12" height="7" rx="2" fill="var(--red)" stroke="#fff" stroke-width="2"/>
          <path d="M11,20 l4,4 l8,-9" fill="none" stroke="#fff" stroke-width="2"/>
          <path d="M9,30 h16" stroke="#fff" stroke-width="2"/>
        </svg>
        TREATEMENTS:
      </h2>
      <ul class="treatments__list">
        <li class="treatments__item"><svg width="12" height="12" viewBox="0 0 12 12" aria-hidden="true"><path d="M6,0 V12 M0,6 H12" stroke="#fff" stroke-width="2"/></svg>Quorvex</li>
        <li class="treatments__item"><svg width="12" height="12" viewBox="0 0 12 12" aria-hidden="true"><path d="M6,0 V12 M0,6 H12" stroke="#fff" stroke-width="2"/></svg>Lip Enhancement</li>
        <li class="treatments__item"><svg width="12" height="12" viewBox="0 0 12 12" aria-hidden="true"><path d="M6,0 V12 M0,6 H12" stroke="#fff" stroke-width="2"/></svg>Chemical Peels</li>
        <li class="treatments__item"><svg width="12" height="12" viewBox="0 0 12 12" aria-hidden="true"><path d="M6,0 V12 M0,6 H12" stroke="#fff" stroke-width="2"/></svg>Facial Fillers</li>
        <li class="treatments__item"><svg width="12" height="12" viewBox="0 0 12 12" aria-hidden="true"><path d="M6,0 V12 M0,6 H12" stroke="#fff" stroke-width="2"/></svg>Non Surgical Face Lift</li>
      </ul>
    </div>
  </section>

  <section class="card card--back" aria-label="Card back">
    <svg class="card__shapes" viewBox="0 0 760 433">
      <path role="img" aria-label="Red band with a subtle geometric pattern" d="M0,0 L440,0 C470,120 590,200 760,240 L760,433 L395,433 C375,250 230,50 0,57 Z" fill="var(--red)"/>
    </svg>

    <p class="owner-name"><span>Penny</span><span>Dowe</span></p>

    <div class="brand">
      <div class="brand__mark"></div>
      <p class="brand__name brand__name--small">Pennington Dowe</p>
      <p class="brand__name brand__name--large">Aesthetics</p>
    </div>

    <ul class="contact">
      <li class="contact__row">4 Brackwell Parade, Surrey, KT9 4WQ
        <svg width="20" height="24" viewBox="0 0 20 24" aria-hidden="true"><path d="M10,23 C4,15 2,12 2,8 a8,8 0 0 1 16,0 c0,4 -2,7 -8,15 Z" fill="none" stroke="#fff" stroke-width="2"/><circle cx="10" cy="8" r="3" fill="#fff"/></svg>
      </li>
      <li class="contact__row">pdabrackwellbookings@gmail.com
        <svg width="22" height="18" viewBox="0 0 22 18" aria-hidden="true"><rect x="1" y="2" width="20" height="14" fill="none" stroke="#fff" stroke-width="2"/><path d="M1,2 L11,10 L21,2" fill="none" stroke="#fff" stroke-width="2"/></svg>
      </li>
      <li class="contact__row contact__row--small">020 8794 2160
        <svg width="20" height="20" viewBox="0 0 20 20" aria-hidden="true"><path d="M4,1 L8,5 L6,8 C7,11 9,13 12,14 L15,12 L19,16 L16,19 C8,18 2,12 1,4 Z" fill="none" stroke="#fff" stroke-width="2"/></svg>
      </li>
      <li class="contact__row contact__row--small">www.penningtondoweaesthetics.co.uk
        <svg width="20" height="20" viewBox="0 0 20 20" aria-hidden="true"><circle cx="10" cy="10" r="8.5" fill="none" stroke="#fff" stroke-width="2"/><path d="M1.5,10 H18.5 M10,1.5 C6,6 6,14 10,18.5 M10,1.5 C14,6 14,14 10,18.5" fill="none" stroke="#fff" stroke-width="1.5"/></svg>
      </li>
    </ul>
  </section>

</main>
</body>
</html>
```